Create a banner for a Gmail email signature

We need a graphic design to use in a solicitor's email signature. The banner will incorporate a head shot of the solicitor as well as the law firm's logo and contact details. The solicitor's photo and law firm's logo are uploaded in the task.

```html
<!DOCTYPE html>
<html lang="en">
<head>
<meta charset="utf-8">
<title>Email Signature Banners</title>
<link href="https://fonts.googleapis.com/css2?family=Outfit:wght@300;400;600;700&display=swap" rel="stylesheet">
<style>
  :root {
    --page: #ffffff;
    --blush: #fbe1da;
    --plum: #8a1c52;
    --ink: #111111;
    --navy: #1b1f4d;
    --ring-dark: #3c2630;
    --white: #ffffff;
    --photo-light: #e9cfb0;
    --photo-mid: #c9a78c;
    --photo-dark: #2c3457;
  }
  * { margin: 0; padding: 0; box-sizing: border-box; }
  html, body {
    width: 1200px;
    height: 1118px;
    overflow: hidden;
    background: var(--page);
    font-family: "Outfit", sans-serif;
  }
  .canvas { position: relative; width: 1200px; height: 1118px; }
  .signature {
    position: absolute;
    left: 175px;
    width: 862px;
    height: 369px;
    background: var(--white);
    overflow: hidden;
  }
  .signature--light { top: 173px; }
  .signature--dark { top: 576px; }
  .signature__backdrop { position: absolute; inset: 0; }
  .signature__name {
    position: absolute;
    left: 316px;
    top: 40px;
    font-size: 57px;
    font-weight: 600;
    line-height: 1;
    letter-spacing: -0.5px;
  }
  .signature__role {
    position: absolute;
    left: 317px;
    top: 102px;
    font-size: 38px;
    font-weight: 300;
    line-height: 1;
  }
  .signature--light .signature__name { color: var(--plum); }
  .signature--light .signature__role { color: var(--navy); }
  .signature--dark .signature__name,
  .signature--dark .signature__role { color: var(--white); }
  .contact {
    position: absolute;
    left: 317px;
    top: 234px;
    color: var(--ink);
    list-style: none;
  }
  .contact__item {
    font-size: 27px;
    font-weight: 300;
    line-height: 34px;
  }
  .contact__item--web {
    font-size: 23px;
    font-weight: 700;
    letter-spacing: 1.2px;
  }
  .firm {
    position: absolute;
    left: 581px;
    top: 250px;
    display: flex;
    align-items: center;
    gap: 10px;
    color: var(--plum);
    font-size: 32px;
    font-weight: 400;
    letter-spacing: 0.5px;
    line-height: 1;
  }
  .firm__dot {
    width: 14px;
    height: 14px;
    border-radius: 50%;
    background: var(--plum);
  }
</style>
</head>
<body>
<main class="canvas">

  <section class="signature signature--light">
    <svg class="signature__backdrop" width="862" height="369" viewBox="0 0 862 369">
      <defs>
        <linearGradient id="portraitToneA" x1="0" y1="0" x2="0" y2="1">
          <stop offset="0" stop-color="var(--photo-light)"/>
          <stop offset="0.6" stop-color="var(--photo-mid)"/>
          <stop offset="1" stop-color="var(--photo-dark)"/>
        </linearGradient>
      </defs>
      <polygon points="0,0 862,0 862,148 0,252" fill="var(--blush)"/>
      <circle cx="160" cy="179" r="123" fill="var(--plum)"/>
      <circle cx="160" cy="179" r="106" fill="url(#portraitToneA)" role="img" aria-label="Head shot of the solicitor"/>
    </svg>
    <h1 class="signature__name">Name Surname</h1>
    <p class="signature__role">Lawyer</p>
    <ul class="contact">
      <li class="contact__item">555.010.234</li>
      <li class="contact__item">Riverton, Md</li>
      <li class="contact__item contact__item--web">www.firmsite.com</li>
    </ul>
    <div class="firm"><span class="firm__dot"></span>HARBOUR LAW</div>
  </section>

  <section class="signature signature--dark">
    <svg class="signature__backdrop" width="862" height="369" viewBox="0 0 862 369">
      <defs>
        <linearGradient id="portraitToneB" x1="0" y1="0" x2="0" y2="1">
          <stop offset="0" stop-color="var(--photo-light)"/>
          <stop offset="0.6" stop-color="var(--photo-mid)"/>
          <stop offset="1" stop-color="var(--photo-dark)"/>
        </linearGradient>
      </defs>
      <polygon points="0,0 862,0 862,148 0,252" fill="var(--plum)"/>
      <circle cx="160" cy="179" r="123" fill="var(--ring-dark)"/>
      <circle cx="160" cy="179" r="106" fill="url(#portraitToneB)" role="img" aria-label="Head shot of the solicitor"/>
    </svg>
    <h2 class="signature__name">Name Surname</h2>
    <p class="signature__role">Lawyer</p>
    <ul class="contact">
      <li class="contact__item">555.010.234</li>
      <li class="contact__item">Riverton, Md</li>
      <li class="contact__item contact__item--web">www.firmsite.com</li>
    </ul>
    <div class="firm"><span class="firm__dot"></span>HARBOUR LAW</div>
  </section>

</main>
</body>
</html>
```